Orthodontic Office Needs New Stationary

We have recently renovated our office and are opening a second location. We need new stationary/branding to go with our new look. We like our logo, but are open to changing the colors to match the office look/feel more.

```html
<!DOCTYPE html>
<html lang="en">
<head>
<meta charset="utf-8">
<title>Harlow &amp; Vance Orthodontics — Letterhead</title>
<link rel="stylesheet" href="https://fonts.googleapis.com/css2?family=Montserrat:wght@400&family=Source+Sans+3:wght@400&display=swap">
<style>
  :root {
    --navy: #182840;
    --navy-soft: #d9dee6;
    --tan: #9e846a;
    --tan-light: #b79f86;
    --paper: #ffffff;
    --ink: #182840;
    --line-white: #ffffff;
  }
  * { margin: 0; padding: 0; box-sizing: border-box; }
  html, body {
    width: 923px;
    height: 1200px;
    overflow: hidden;
    background: var(--paper);
  }
  .letterhead {
    position: relative;
    width: 923px;
    height: 1200px;
    background: var(--paper);
    overflow: hidden;
  }
  .header-band {
    position: absolute;
    left: 157px;
    top: 0;
    width: 766px;
    height: 135px;
    background: var(--tan);
  }
  .side-block {
    position: absolute;
    left: 0;
    top: 0;
    width: 157px;
    height: 327px;
    background: var(--navy);
  }
  .header-art {
    position: absolute;
    left: 0;
    top: 0;
    width: 923px;
    height: 330px;
  }
  .practice-name {
    position: absolute;
    left: 52px;
    top: 44px;
    color: var(--line-white);
    font-family: "Montserrat", sans-serif;
    font-weight: 400;
    line-height: 1;
  }
  .practice-name__title {
    display: block;
    font-size: 29px;
    letter-spacing: 0.01em;
  }
  .practice-name__subtitle {
    display: block;
    margin-top: 3px;
    font-size: 17px;
    letter-spacing: 0.66em;
  }
  .footer-ornament {
    position: absolute;
    left: 159px;
    top: 1074px;
    width: 659px;
    height: 32px;
    background: var(--navy-soft);
  }
  .contact-line {
    position: absolute;
    top: 1128px;
    font-family: "Source Sans 3", sans-serif;
    font-size: 11.8px;
    color: var(--ink);
    white-space: nowrap;
  }
  .contact-line--address { left: 216px; }
  .contact-line--phone   { left: 474px; }
  .contact-line--web     { left: 591px; }
</style>
</head>
<body>
<main class="letterhead">
  <div class="header-band"></div>
  <div class="side-block"></div>

  <svg class="header-art" viewBox="0 0 923 330">
    <line x1="354" y1="69" x2="738" y2="69" stroke="var(--line-white)" stroke-width="2"/>
    <circle cx="779" cy="69" r="41" fill="var(--tan-light)" role="img" aria-label="Round smiling emoji icon"/>
    <line x1="76" y1="109" x2="76" y2="208" stroke="var(--line-white)" stroke-width="1.5"/>
    <circle cx="74" cy="249" r="41" fill="none" stroke="var(--line-white)" stroke-width="1.5"/>
  </svg>

  <h1 class="practice-name">
    <span class="practice-name__title">HARLOW &amp; VANCE</span>
    <span class="practice-name__subtitle">ORTHODONTICS</span>
  </h1>

  <div class="footer-ornament" role="img" aria-label="Decorative braces bracket and wire ornament"></div>

  <p class="contact-line contact-line--address">4180 Cedar Row #112, Millbrook State 40217</p>
  <p class="contact-line contact-line--phone">555-314-2807</p>
  <p class="contact-line contact-line--web">www.brightlinesmiles.com</p>
</main>
</body>
</html>
```